Design a homepage graphic to show a system journey

We have a software package for parents to update student information and manage school excursions we have attached a concept we like but are open to other ideas so long as they fit the following criteria.
1 It needs to be landscape across the page
2. They are showing a series of processes, each step has its own colour, see below
2.1 The first process is a parent updating their own and students information and approving excursions
2.2 The school then creates and manages the excursion this includes a compliance component
2.3 The school conducts the activity it should show some activity type pictures
2.4 Students return safely to school
3 There can be text boxes within the image to clarify functionality
4. The picture should make anyone watching it understand there is a series of
linked processes the system provides i.e. a journey
There should be the ability to click on each component to link to a specific part of the pager lower down, e.g if the person wanted to look at the school part by clicking on the school it would take them to more information, that information already exists so is not required.
Please review the attached concept diagram and use this a potential guide.
Schools
1 page

```html
<!DOCTYPE html>
<html lang="en">
<head>
<meta charset="utf-8">
<title>School Excursion Journey</title>
<link rel="stylesheet" href="https://fonts.googleapis.com/css2?family=Poppins:wght@400;500&display=swap">
<style>
  :root {
    --bg: #ffffff;
    --road: #474f57;
    --road-shade: #d9dde1;
    --dash: #ffffff;
    --ink: #333a40;
    --muted: #555;
    --pink: #ff8fd0;
    --green: #a6bb5a;
    --purple: #c062cf;
    --blue: #14b0dc;
    --teal: #19cfa6;
    --yellow: #fdc956;
    --rule: #dff0f7;
  }
  * { margin: 0; padding: 0; box-sizing: border-box; }
  html, body { width: 1200px; height: 675px; overflow: hidden; background: var(--bg); }
  .journey {
    position: relative; width: 1200px; height: 675px;
    font-family: "Poppins", sans-serif; color: var(--ink);
  }
  .scene { position: absolute; border-radius: 10px; }
  .scene--parents  { left: 38px;  top: 209px; width: 81px;  height: 100px; background: linear-gradient(160deg, #f4c9b5, #4b6fa8); }
  .scene--student  { left: 200px; top: 303px; width: 66px;  height: 119px; background: linear-gradient(180deg, #f6d3c1, #ee5d4f 55%, #8ea6e6); }
  .scene--walkers  { left: 341px; top: 309px; width: 69px;  height: 66px;  background: linear-gradient(160deg, #f9d1ef, #3d5a9a); }
  .scene--shelf    { left: 462px; top: 240px; width: 88px;  height: 57px;  background: linear-gradient(120deg, #9bb3ea, #f1f1f1); }
  .scene--reader   { left: 612px; top: 334px; width: 69px;  height: 107px; background: linear-gradient(180deg, #f3c7c0, #9fd9bf 50%, #b7b0a8); }
  .scene--sailing  { left: 734px; top: 306px; width: 97px;  height: 81px;  background: linear-gradient(120deg, #3f6ec0, #7fd2ef); }
  .scene--play     { left: 887px; top: 315px; width: 91px;  height: 66px;  background: linear-gradient(160deg, #f7e6c6, #f6c945); }
  .scene--return   { left: 1016px; top: 309px; width: 147px; height: 138px; background: linear-gradient(150deg, #d8eef4, #d8363a 55%, #f08a2c); }

  .road { position: absolute; left: 0; top: 0; width: 1200px; height: 675px; }
  .road__line { fill: none; stroke-linecap: butt; stroke-linejoin: round; }
  .road__shade { stroke: var(--road-shade); stroke-width: 34; transform: translate(8px, 6px); }
  .road__base { stroke: var(--road); stroke-width: 34; }
  .road__dash { stroke: var(--dash); stroke-width: 4; stroke-dasharray: 10 11; }
  .pin__stem { fill: currentColor; stroke: none; }
  .pin__ring { fill: #fff; stroke: currentColor; stroke-width: 6; }

  .step { position: absolute; text-decoration: none; color: inherit; }
  .step__num {
    position: absolute; width: 72px; height: 72px; margin: -36px 0 0 -36px;
    display: flex; align-items: center; justify-content: center;
    font-size: 23px; font-weight: 500; color: #222;
  }
  .step__label {
    position: absolute; font-size: 15px; line-height: 18px;
    letter-spacing: 0.5px; text-transform: uppercase; white-space: nowrap; color: var(--ink);
  }
  .code-mark { position: absolute; left: 1146px; top: 636px; font-size: 14px; color: var(--muted); }
  .base-rule { position: absolute; left: 24px; top: 671px; width: 1104px; height: 3px; background: var(--rule); }
</style>
</head>
<body>
<main class="journey">
  <div class="scene scene--parents" role="img" aria-label="Illustration of two parents taking a selfie"></div>
  <div class="scene scene--student" role="img" aria-label="Illustration of a happy student balancing books"></div>
  <div class="scene scene--walkers" role="img" aria-label="Illustration of two children walking with school bags"></div>
  <div class="scene scene--shelf" role="img" aria-label="Illustration of a child at a bookshelf"></div>
  <div class="scene scene--reader" role="img" aria-label="Illustration of a child holding an open book"></div>
  <div class="scene scene--sailing" role="img" aria-label="Illustration of a child beside a sailing ship"></div>
  <div class="scene scene--play" role="img" aria-label="Illustration of a child reading among toys"></div>
  <div class="scene scene--return" role="img" aria-label="Illustration of children running back to the school building"></div>

  <svg class="road" viewBox="0 0 1200 675" aria-hidden="true">
    <defs>
      <path id="route" d="M24 341 H128 A33 33 0 0 0 161 308 A33 33 0 0 1 194 275 H267 A33 33 0 0 1 300 308 V372 A33 33 0 0 0 333 405 H404 A33 33 0 0 0 437 372 V242 A33 33 0 0 1 470 209 H542 A33 33 0 0 1 575 242 V436 A33 33 0 0 0 608 469 H681 A33 33 0 0 0 714 436 V308 A33 33 0 0 1 747 275 H820 A33 33 0 0 1 853 308 V372 A33 33 0 0 0 886 405 H958 A33 33 0 0 0 991 373 A32 32 0 0 1 1023 341 H1128"/>
      <g id="pin">
        <path class="pin__stem" d="M-11 33 Q-3 62 0 105 Q3 62 11 33 Z"/>
        <circle class="pin__ring" r="38"/>
      </g>
    </defs>
    <use href="#route" class="road__line road__shade"/>
    <use href="#route" class="road__line road__base"/>
    <use href="#route" class="road__line road__dash"/>

    <use href="#pin" style="color:var(--pink)"   transform="translate(71 476) rotate(180)"/>
    <use href="#pin" style="color:var(--green)"  transform="translate(231 150)"/>
    <use href="#pin" style="color:var(--purple)" transform="translate(369 514) rotate(180)"/>
    <use href="#pin" style="color:var(--blue)"   transform="translate(506 84)"/>
    <use href="#pin" style="color:var(--teal)"   transform="translate(646 595) rotate(180)"/>
    <use href="#pin" style="color:var(--pink)"   transform="translate(783 150)"/>
    <use href="#pin" style="color:var(--yellow)" transform="translate(921 530) rotate(180)"/>
    <use href="#pin" style="color:var(--purple)" transform="translate(1071 199)"/>
  </svg>

  <a class="step" href="#parent-information">
    <span class="step__num" style="left:71px;top:476px">1</span>
    <span class="step__label" style="left:87px;top:382px">Parent<br>Information</span>
  </a>
  <a class="step" href="#student-information">
    <span class="step__num" style="left:231px;top:150px">2</span>
    <span class="step__label" style="left:254px;top:196px">Student<br>Information</span>
  </a>
  <a class="step" href="#approving-excursion">
    <span class="step__num" style="left:369px;top:514px">3</span>
    <span class="step__label" style="left:394px;top:433px">Approving<br>Excursion</span>
  </a>
  <a class="step" href="#school-accepts">
    <span class="step__num" style="left:506px;top:84px">4</span>
    <span class="step__label" style="left:529px;top:137px">The school accepts<br>all the update</span>
  </a>
  <a class="step" href="#school-manages">
    <span class="step__num" style="left:646px;top:595px">5</span>
    <span class="step__label" style="left:667px;top:500px">The school manages<br>the excursion</span>
  </a>
  <a class="step" href="#school-takes">
    <span class="step__num" style="left:783px;top:150px">6</span>
    <span class="step__label" style="left:802px;top:199px">The school takes the<br>children to the excursion</span>
  </a>
  <a class="step" href="#school-activity">
    <span class="step__num" style="left:921px;top:530px">7</span>
    <span class="step__label" style="left:946px;top:434px">The school<br>conducts<br>activity</span>
  </a>
  <a class="step" href="#students-return">
    <span class="step__num" style="left:1071px;top:199px">8</span>
    <span class="step__label" style="left:1084px;top:247px">Students<br>return to<br>the school</span>
  </a>

  <span class="code-mark">C44</span>
  <div class="base-rule"></div>
</main>
</body>
</html>
```